Rack Card Design Project

www.northlodgefreightway.com I am looking for a Rack Card for our Pick up/drop off and shipping purposes. So listed below are things I want on it.
Name, Address, Phone number, Credit Card info, Pickup or Drop off location, What the Item is, How many pieces or boxes. We are a hunting/ fishing company that specializes in Cold Storage and shipping of peoples fish and animals from Alaska. I added our company logo and also a Design of a Rack card so you can see what we are looking for.

```html
<!DOCTYPE html>
<html lang="en">
<head>
<meta charset="utf-8">
<title>North Lodge Freightway Rack Card</title>
<link href="https://fonts.googleapis.com/css2?family=Open+Sans:wght@400;600;700;800&family=Roboto+Slab:wght@400&display=swap" rel="stylesheet">
<style>
:root{
  --bg:#bcbdc0;
  --red:#c1272d;
  --red-dark:#a91f25;
  --ink:#333333;
  --muted:#555555;
  --field:#f1f1f2;
  --swoosh:#a7a9ac;
  --white:#ffffff;
}
*{box-sizing:border-box;margin:0;padding:0}
html,body{width:1200px;height:1148px;overflow:hidden;background:var(--bg);font-family:"Open Sans",sans-serif}
.stage{position:absolute;left:0;top:0;width:1100px;height:1069px;transform:scale(1.0909,1.0739);transform-origin:0 0}
.card{position:absolute;top:72px;width:427px;height:925px;background:var(--white);box-shadow:6px 8px 10px rgba(0,0,0,.35);overflow:hidden}
.card--form{left:93px}
.card--promo{left:578px}
.abs{position:absolute}
.shape{position:absolute;left:0;top:0;width:427px;height:925px}
.brand{position:absolute;left:0;width:427px;text-align:center;color:var(--ink);font-weight:800;letter-spacing:.5px;line-height:1.1;z-index:2}
.brand__sub{display:block;color:var(--red);font-weight:800;letter-spacing:3px}
.brand__mark{display:inline-block;width:14px;height:14px;border-radius:50%;background:var(--ink);vertical-align:middle;margin-right:8px;position:relative;top:-3px}
.band-title{left:0;width:427px;text-align:center;color:var(--white);font-size:19px;font-weight:400;top:184px}
.fields{left:24px;top:226px;width:375px}
.field{height:21px;margin-bottom:3.4px;background:var(--field);font-size:11px;color:var(--muted);padding:3px 8px;position:relative}
.field__aside{position:absolute;left:236px;top:3px}
.check{display:inline-block;width:11px;height:11px;border:2px solid var(--red);border-radius:2px;vertical-align:-1px;margin-right:6px;background:var(--white)}
.cards-row{left:33px;top:427px;font-size:11px;color:var(--muted)}
.cards-row span{margin-right:14px}
.notice{left:0;top:448px;width:427px;height:62px;background:var(--red);color:var(--white);text-align:center;font-size:15px;font-weight:600;line-height:21px;padding-top:10px}
.notice-sub{left:0;top:515px;width:427px;text-align:center;color:var(--red);font-size:10.5px;font-weight:600}
.checks{left:33px;font-size:11px;color:var(--muted);line-height:18px}
.pill{left:24px;width:375px;height:22px;border-radius:11px;background:var(--red);color:var(--white);font-size:10.5px;font-weight:700;text-align:center;line-height:22px}
.lines{left:33px;top:622px;width:366px;font-size:11px;color:var(--muted)}
.line{display:flex;align-items:flex-end;height:24px}
.line__rule{flex:1;border-bottom:1px solid var(--muted);margin:0 0 4px 3px}
.options{top:802px;font-size:11px;color:var(--muted);line-height:15px}
.contact{left:0;width:427px;text-align:center;font-size:10.5px;line-height:15px;z-index:2}
.contact--light{top:868px;color:var(--white)}
.contact--red{top:868px;color:var(--red-dark)}
.contact strong{font-weight:700}
.photo{left:0;top:195px;width:427px;height:372px;background:linear-gradient(160deg,#8c8a72 0%,#6b6247 40%,#4b3f30 70%,#7a6a4c 100%)}
.promo-body{left:0;top:567px;width:427px;height:300px;background:var(--red)}
.intro{left:10px;top:584px;width:407px;text-align:center;color:var(--white);font-size:11.5px;line-height:16px}
.services-pill{left:80px;top:641px;width:267px;height:27px;border-radius:14px;background:var(--white);color:var(--red);font-family:"Roboto Slab",serif;font-size:18px;text-align:center;line-height:27px}
.service-text{color:var(--white);font-size:8px;line-height:10px;width:148px}
.service-text ul{list-style:none}
.social{top:822px;width:22px;height:22px;border:1.5px solid var(--white);border-radius:50%}
</style>
</head>
<body>
<div class="stage">

  <section class="card card--form">
    <svg class="shape" viewBox="0 0 427 925" aria-hidden="true">
      <path d="M0 142 Q213 172 427 140" fill="none" stroke="var(--swoosh)" stroke-width="6"/>
      <path d="M0 154 Q213 184 427 152 L427 220 L0 220Z" fill="var(--red)"/>
      <path d="M0 858 Q213 842 427 856" fill="none" stroke="var(--swoosh)" stroke-width="5"/>
      <path d="M0 866 Q213 850 427 864 L427 925 L0 925Z" fill="var(--red)"/>
    </svg>
    <div class="brand" style="top:82px;font-size:26px"><span class="brand__mark"></span>NORTH LODGE<span class="brand__sub" style="font-size:13px">FREIGHTWAY</span></div>
    <h1 class="abs band-title">SERVICES / SHIPPING INFORMATION</h1>

    <div class="abs fields">
      <div class="field">Lodge:<span class="field__aside">Date:</span></div>
      <div class="field">Name:</div>
      <div class="field">Address:</div>
      <div class="field"></div>
      <div class="field">Cell Phone:</div>
      <div class="field">Home Phone:</div>
      <div class="field">Work Phone:</div>
      <div class="field">Credit Card No:<span class="field__aside">Exp:</span></div>
    </div>
    <div class="abs cards-row"><span><i class="check"></i>Northpay</span><span><i class="check"></i>Cardix</span></div>

    <div class="abs notice">Please place this completed card<br>in a zip-top bag</div>
    <div class="abs notice-sub">PLEASE CHECK APPROPRIATE BOXES</div>
    <div class="abs checks" style="top:534px">
      <div><i class="check"></i>Ship within USA</div>
      <div><i class="check"></i>Ship within Canada (additional charges may apply)</div>
      <div><i class="check"></i>Will Pick Up. Pick Up Date___________________</div>
    </div>

    <div class="abs pill" style="top:596px">SELECT DROP OFF SERVICE NEEDED</div>
    <div class="abs lines">
      <div class="line"><i class="check"></i>Taxidermist:<span class="line__rule"></span></div>
      <div class="line"><i class="check"></i>Meat Processor:<span class="line__rule"></span></div>
      <div class="line"><i class="check"></i>Airport:<span class="line__rule" style="flex:0 0 158px"></span>&nbsp;&nbsp;&nbsp;Time:<span class="line__rule"></span></div>
      <div class="line"><i class="check"></i>Mail:<span class="line__rule"></span></div>
      <div class="line"><i class="check"></i>Cold Storage:<span class="line__rule"></span></div>
      <div class="line"><i class="check"></i>Hotel:<span class="line__rule"></span></div>
    </div>

    <div class="abs pill" style="top:773px">SHIPPING OPTIONS</div>
    <div class="abs options" style="left:33px">
      <div><i class="check"></i>Truck Ground Shipping</div>
      <div><i class="check"></i>Tundra Air Cargo</div>
      <div><i class="check"></i>International Shipping</div>
    </div>
    <div class="abs options" style="left:212px">
      <div><i class="check"></i>Coastal Post</div>
      <div><i class="check"></i>Overnight Shipping</div>
      <div><i class="check"></i>ParcelRun, QuickFreight</div>
    </div>

    <div class="abs contact contact--light">
      <strong><svg width="10" height="10" viewBox="0 0 24 24" style="vertical-align:-1px"><circle cx="12" cy="12" r="11" fill="none" stroke="#fff" stroke-width="2"/><path d="M8 6l2 0 1 3-1.5 1.2a8 8 0 0 0 4 4L15 12.5l3 1v2.2c0 .8-1 1.3-2 1.3C11 17 7 13 7 8c0-1 .5-2 1-2z" fill="#fff"/></svg> (907) 555-0148</strong><br>
      2870 Birchwood Loop Anchorage, Ak 99508<br>
      northlodgefreightway@mailbox.com | www.northlodgefreightway.com
    </div>
  </section>

  <section class="card card--promo">
    <div class="abs photo" role="img" aria-label="Photo of two hunters in camouflage kneeling beside a large bull moose in an autumn forest"></div>
    <svg class="shape" viewBox="0 0 427 925" aria-hidden="true">
      <path d="M0 0 L427 0 L427 196 Q213 182 0 214Z" fill="var(--white)"/>
      <path d="M0 208 Q213 176 427 192" fill="none" stroke="var(--swoosh)" stroke-width="6"/>
      <path d="M0 866 Q213 846 427 860" fill="none" stroke="var(--swoosh)" stroke-width="6"/>
      <path d="M0 872 Q213 852 427 866 L427 925 L0 925Z" fill="var(--white)"/>
    </svg>
    <div class="brand" style="top:104px;font-size:32px"><span class="brand__mark"></span>NORTH LODGE<span class="brand__sub" style="font-size:16px">FREIGHTWAY</span></div>

    <div class="abs promo-body"></div>
    <p class="abs intro">We are a small business located in Anchorage, Alaska and are dedicated to helping you ship, store, and transport your Alaskan trophy home.</p>
    <div class="abs services-pill">OUR SERVICES</div>

    <svg class="abs" style="left:0;top:680px" width="427" height="130" viewBox="0 0 427 130" aria-hidden="true">
      <g fill="none" stroke="#fff" stroke-width="2">
        <circle cx="38" cy="31" r="22"/><circle cx="243" cy="31" r="22"/>
        <circle cx="38" cy="103" r="22"/><circle cx="243" cy="103" r="22"/>
      </g>
      <g fill="#fff">
        <rect x="24" y="21" width="28" height="20"/>
        <path d="M229 27l14-6 14 6v16l-14 6-14-6z"/>
        <rect x="23" y="95" width="19" height="14"/><path d="M42 99h7l4 5v5H42z"/>
        <circle cx="29" cy="111" r="3"/><circle cx="47" cy="111" r="3"/>
        <rect x="233" y="90" width="18" height="24"/>
      </g>
      <g stroke="var(--red)" stroke-width="1.2">
        <path d="M28 23v16M32 23v16M36 23v16M40 23v16M44 23v16M48 23v16"/>
        <path d="M229 27l14 6 14-6M243 33v16"/>
        <path d="M236 96h12M236 101h12M236 106h8"/>
      </g>
    </svg>
    <div class="abs service-text" style="left:70px;top:692px">If you are all done fishing or hunting and need a place to store your meat before your flight we have you covered.</div>
    <div class="abs service-text" style="left:275px;top:692px"><ul><li>• Crating</li><li>• Fish Boxes</li><li>• Foam Molded Boxes</li><li>• Custom Packaging</li></ul></div>
    <div class="abs service-text" style="left:70px;top:766px"><ul><li>• Airport Pickup or Drop off</li><li>• Meat Pickup and Drop off</li><li>• Pickup and Drop off at Processors<br>&nbsp;&nbsp;or Taxidermist</li></ul></div>
    <div class="abs service-text" style="left:275px;top:766px">If you have a service you need and you don't see it listed here please contact us</div>

    <div class="abs social" style="left:185px"></div>
    <div class="abs social" style="left:218px"></div>

    <div class="abs contact contact--red">
      <strong>(907) 555-0148</strong><br>
      2870 Birchwood Loop Anchorage, Ak 99508<br>
      northlodgefreightway@mailbox.com | www.northlodgefreightway.com
    </div>
  </section>

</div>
</body>
</html>
```